Flowy subpage design wanted for a modern tax/accounting firm in Switzerland

--- Introduction ---
We are a tax and accounting firm in Switzerland. We provide services for expats living in Switzerland, our service is quite exclusive and modern (digital).

We just relaunched our website www.fiscaverde.ch and are happy with the design, so the desired subpage (more details below) should of course fit in.

--- Main brief ---
Please see Word File attached. The page has to include the whole text (11 chapters). A very intuitive, flowy design on only one subpage (not one page per chapter) is a MUST. Also, it is key that the design is supporting the content of the individual chapters, so it would be advantageous if you'd have a good unterstanding of the text attached.

--- Further information ---
A similar example would be this one: https://www2.brennmark.com/ch/en/pages/tax/articles/living-working-switzerland.html

This one is similar in what concerns the content, but NOT what we are looking for designwise. It is very simple and looks "thrown together", just not aesthetically pleasing in our opinion.

--- Final thoughts ---
- If you blow our minds with your design, we will certainly have future work for you.
- Our clients are between 20-50 years old, well educated, high income / high wealth, English speaking and living in Switzerland.
- CI/CD information:
Fonts
Montserrat regular / medium italic / bold
Colors
White #ffffffff
Darkblue #0a2b46
Darkblue 25% #b5bfc8
Darkblue 50% #8595a4
Greenblue #0d4261

We are looking forward to your designs!
Updates

Thank you very much for the submitted designs and your efforts. Unfortunately, none of the designs meet our expectations so far. Please note the following: - Designs that do not take CI into account will not be looked at more closely. - We have received many simple designs with very simple structure and accordion elements. But more important than the simple structure is an eye-catching design! Make it flowy and beautiful - We don't want pictures of Swiss vehicles, passes or other pictures that don't actively support the text. If you can make an illustration that really fits the context, fine, otherwise better leave it without. Thank you

Target Market(s)

Expats living in Switzerland. High income earners / high net worth individuals

Industry/Entity Type

tax/accounting

Number of Pages Required

1 page

Font styles to use
Other font styles liked:
• Montserrat

Colors
0054AA
0677BA
7BADD7
CADEEF
E8F1F8

Requirements
Must have
• based on general website design
Nice to have
• intuitive, flowy, attractive representation of much text
Should not have
• basic copy/paste of the text in sections :)

```html
<!DOCTYPE html>
<html lang="en">
<head>
<meta charset="utf-8">
<title>Switzerland – Fiscaverde Advisory</title>
<link href="https://fonts.googleapis.com/css2?family=Montserrat:ital,wght@0,300;0,400;0,500;0,600;0,700;1,500&display=swap" rel="stylesheet">
<style>
:root{
  --navy:#0a2b46;
  --greenblue:#0d4261;
  --navy-25:#b5bfc8;
  --navy-50:#8595a4;
  --blue:#0054aa;
  --blue-mid:#0677ba;
  --blue-soft:#7badd7;
  --blue-pale:#cadeef;
  --blue-ice:#e8f1f8;
  --white:#ffffff;
  --grey-band:#e9ecef;
}
*{box-sizing:border-box;margin:0;padding:0}
html,body{width:1200px;height:4184px;overflow:hidden}
body{position:relative;font-family:'Montserrat',sans-serif;color:var(--navy);background:var(--white)}
.abs{position:absolute}
.chev{position:absolute;right:6px;top:50%;width:14px;height:9px;margin-top:-4px}
/* header */
.site-header{position:absolute;left:0;top:0;width:1200px;height:62px;z-index:3}
.brand{left:141px;top:10px;display:flex;align-items:center;gap:8px}
.brand-dot{width:38px;height:38px;border-radius:50%;border:3px solid var(--navy)}
.brand-name{font-weight:600;font-size:15px;line-height:17px;letter-spacing:.5px;color:var(--navy)}
.nav a{position:absolute;top:19px;font-size:12px;color:var(--navy);text-decoration:none}
.nav a.active{font-weight:700}
.nav-underline{left:547px;top:60px;width:123px;height:3px;background:var(--greenblue)}
.btn-calc{left:989px;top:11px;width:114px;height:31px;background:var(--navy);color:#fff;font-size:11px;font-weight:700;display:flex;align-items:center;justify-content:center;gap:6px}
.header-rule{left:26px;top:62px;width:1130px;height:1px;background:var(--navy-25)}
/* hero */
.hero-bg{left:0;top:0;width:1200px;height:560px}
.hero-title{left:122px;top:110px;font-size:41px;font-weight:700;letter-spacing:.5px}
.toc-item{position:absolute;display:flex;align-items:center;gap:10px;font-size:13.5px;font-weight:700;text-transform:uppercase;letter-spacing:.2px;line-height:16px}
.toc-num{flex:none;width:26px;height:26px;border-radius:50%;background:var(--navy);color:#fff;font-size:10px;display:flex;align-items:center;justify-content:center}
/* generic */
.illus{position:absolute}
.h-light{font-weight:300}
.lead{font-size:12.5px;line-height:21px;color:var(--greenblue)}
.acc{position:absolute;border-bottom:1px solid var(--navy-25);height:49px;display:flex;align-items:center;gap:14px;font-size:14px;font-weight:700;color:var(--greenblue)}
.acc svg.icon{width:30px;height:26px;flex:none}
.dark .acc{border-color:rgba(255,255,255,.35);color:#fff}
/* dark band */
.band-dark{left:0;top:1091px;width:1200px;height:644px;background:linear-gradient(160deg,var(--greenblue),var(--navy))}
.band-grey{left:0;top:2347px;width:1200px;height:593px;background:var(--grey-band)}
.band-dark2{left:0;top:3537px;width:1200px;height:548px;background:linear-gradient(160deg,var(--greenblue),var(--navy))}
</style>
</head>
<body>

<!-- HERO -->
<svg class="abs hero-bg" viewBox="0 0 1200 560" preserveAspectRatio="none">
  <defs><linearGradient id="heroGrad" x1="0" y1="0" x2="1" y2="1">
    <stop offset="0" stop-color="#d7e5f1"/><stop offset="1" stop-color="#eef4f9"/></linearGradient></defs>
  <polygon points="0,0 1200,0 1200,430 0,528" fill="url(#heroGrad)"/>
  <polygon points="625,490 1200,430 1200,548" fill="var(--navy)"/>
</svg>

<header class="site-header">
  <div class="abs brand"><span class="brand-dot"></span><span class="brand-name">FISCAVERDE<br>ADVISORY</span></div>
  <nav class="nav">
    <a style="left:343px">About Us</a>
    <a style="left:438px">Tax Services</a>
    <a class="active" style="left:547px">Business Packages</a>
    <a style="left:703px">Swiss Tax Guide</a>
    <a style="left:835px">About us</a>
    <a style="left:926px">Blog</a>
  </nav>
  <div class="abs nav-underline"></div>
  <div class="abs btn-calc"><svg width="10" height="13" viewBox="0 0 10 13"><rect x="0.5" y="0.5" width="9" height="12" fill="none" stroke="#fff"/><rect x="2" y="2" width="6" height="3" fill="#fff"/></svg>Calculate</div>
</header>
<div class="abs header-rule"></div>

<h1 class="abs hero-title">SWITZERLAND</h1>
<div class="toc-item" style="left:122px;top:190px"><span class="toc-num">01</span>Life in Switzerland</div>
<div class="toc-item" style="left:122px;top:231px"><span class="toc-num">02</span>Switzerland - a brief overview of the alpine country</div>
<div class="toc-item" style="left:122px;top:273px"><span class="toc-num">03</span>Immigrating to Switzerland - these options are available</div>
<div class="toc-item" style="left:122px;top:315px"><span class="toc-num">04</span>Labor law in Switzerland - an overview</div>
<div class="toc-item" style="left:122px;top:372px"><span class="toc-num">05</span>Double taxation agreements between<br>Switzerland and other countries</div>
<div class="toc-item" style="left:723px;top:190px"><span class="toc-num">06</span>Indirect taxes in Switzerland</div>
<div class="toc-item" style="left:723px;top:232px"><span class="toc-num">07</span>Other federal taxes in Switzerland</div>
<div class="toc-item" style="left:723px;top:274px"><span class="toc-num">08</span>Rent and buy in Switzerland</div>
<div class="toc-item" style="left:723px;top:317px"><span class="toc-num">09</span>Childcare in Switzerland</div>
<div class="toc-item" style="left:723px;top:359px"><span class="toc-num">10</span>Public transportation</div>
<div class="toc-item" style="left:723px;top:401px"><span class="toc-num">11</span>Recreation</div>

<!-- LIFE -->
<section>
  <div class="illus" role="img" aria-label="Line illustration of a Swiss city skyline labelled living, general, public transport and education" style="left:94px;top:641px;width:483px;height:374px;background:radial-gradient(ellipse at 50% 60%,var(--blue-pale),var(--blue-ice) 60%,#fff 85%)"></div>
  <h2 class="abs" style="left:617px;top:602px;font-size:36px;font-weight:700">Life in <span class="h-light">Switzerland</span></h2>
  <p class="abs lead" style="left:617px;top:660px;width:440px">To give you a small impression of what to expect when living in Switzerland, we have put together some topics for you to make your new start in Switzerland as pleasant as possible.</p>
  <div class="acc" style="left:620px;top:741px;width:428px"><svg class="icon" viewBox="0 0 30 26"><circle cx="15" cy="13" r="11" fill="none" stroke="var(--greenblue)" stroke-width="1.4"/><ellipse cx="15" cy="13" rx="5" ry="11" fill="none" stroke="var(--greenblue)" stroke-width="1.2"/><line x1="4" y1="13" x2="26" y2="13" stroke="var(--greenblue)" stroke-width="1.2"/></svg>General<svg class="chev" viewBox="0 0 14 9"><polyline points="1,1 7,7 13,1" fill="none" stroke="var(--greenblue)" stroke-width="1.6"/></svg></div>
  <div class="acc" style="left:620px;top:790px;width:428px"><svg class="icon" viewBox="0 0 30 26"><line x1="5" y1="3" x2="5" y2="24" stroke="var(--greenblue)" stroke-width="1.4"/><rect x="5" y="4" width="20" height="13" fill="none" stroke="var(--greenblue)" stroke-width="1.4"/><path d="M15 7v7M11.5 10.5h7" stroke="var(--greenblue)" stroke-width="1.4"/></svg>Living in Switzerland<svg class="chev" viewBox="0 0 14 9"><polyline points="1,1 7,7 13,1" fill="none" stroke="var(--greenblue)" stroke-width="1.6"/></svg></div>
  <div class="acc" style="left:620px;top:839px;width:428px"><svg class="icon" viewBox="0 0 30 26"><polygon points="15,4 28,10 15,16 2,10" fill="none" stroke="var(--greenblue)" stroke-width="1.4"/><path d="M8 13v6c4 3 10 3 14 0v-6" fill="none" stroke="var(--greenblue)" stroke-width="1.4"/></svg>The education system in Switzerland<svg class="chev" viewBox="0 0 14 9"><polyline points="1,1 7,7 13,1" fill="none" stroke="var(--greenblue)" stroke-width="1.6"/></svg></div>
  <div class="acc" style="left:620px;top:888px;width:428px"><svg class="icon" viewBox="0 0 30 26"><circle cx="15" cy="13" r="11" fill="none" stroke="var(--greenblue)" stroke-width="1.4"/><circle cx="15" cy="13" r="4" fill="none" stroke="var(--greenblue)" stroke-width="1.4"/><path d="M4 11h7M19 11h7M15 17v7" stroke="var(--greenblue)" stroke-width="1.4"/></svg>Driving in Switzerland<svg class="chev" viewBox="0 0 14 9"><polyline points="1,1 7,7 13,1" fill="none" stroke="var(--greenblue)" stroke-width="1.6"/></svg></div>
  <div class="acc" style="left:620px;top:937px;width:428px"><svg class="icon" viewBox="0 0 30 26"><rect x="3" y="6" width="24" height="12" rx="3" fill="none" stroke="var(--greenblue)" stroke-width="1.4"/><path d="M7 9h6v4H7zM16 9h6v4h-6z" fill="none" stroke="var(--greenblue)" stroke-width="1.2"/><circle cx="9" cy="20" r="2" fill="var(--greenblue)"/><circle cx="21" cy="20" r="2" fill="var(--greenblue)"/></svg>Public transport in Switzerland<svg class="chev" viewBox="0 0 14 9"><polyline points="1,1 7,7 13,1" fill="none" stroke="var(--greenblue)" stroke-width="1.6"/></svg></div>
</section>

<!-- OVERVIEW -->
<section class="dark">
  <div class="abs band-dark"></div>
  <h2 class="abs" style="left:162px;top:1175px;color:#fff;font-size:36px;line-height:36px;font-weight:700">Switzerland<br><span class="h-light">a brief overview of the<br>Alpine country</span></h2>
  <p class="abs lead" style="left:162px;top:1306px;width:410px;color:#e4ebf1">Every year, Switzerland attracts many new citizens who want to settle there temporarily or long-term, and not without reason, because life in Switzerland is characterized by a high quality. If you are also thinking of settling here, we would like to introduce you to the country in the following.</p>
  <div class="acc" style="left:169px;top:1442px;width:386px"><svg class="icon" viewBox="0 0 30 26"><polygon points="15,3 27,9 3,9" fill="none" stroke="#fff" stroke-width="1.3"/><path d="M6 11v10M12 11v10M18 11v10M24 11v10M3 23h24" stroke="#fff" stroke-width="1.3"/></svg>A strong federation<svg class="chev" viewBox="0 0 14 9"><polyline points="1,1 7,7 13,1" fill="none" stroke="#fff" stroke-width="1.6"/></svg></div>
  <div class="acc" style="left:169px;top:1484px;width:386px"><svg class="icon" viewBox="0 0 30 26"><circle cx="15" cy="6" r="3" fill="none" stroke="#fff" stroke-width="1.3"/><circle cx="9" cy="14" r="3" fill="none" stroke="#fff" stroke-width="1.3"/><circle cx="21" cy="14" r="3" fill="none" stroke="#fff" stroke-width="1.3"/><path d="M3 24c0-4 12-4 12 0M15 24c0-4 12-4 12 0" fill="none" stroke="#fff" stroke-width="1.3"/></svg>A diverse population structure<svg class="chev" viewBox="0 0 14 9"><polyline points="1,1 7,7 13,1" fill="none" stroke="#fff" stroke-width="1.6"/></svg></div>
  <div class="acc" style="left:169px;top:1526px;width:386px"><svg class="icon" viewBox="0 0 30 26"><rect x="4" y="4" width="22" height="18" fill="none" stroke="#fff" stroke-width="1.3"/><polyline points="6,18 12,12 17,15 24,7" fill="none" stroke="#fff" stroke-width="1.3"/></svg>Excellent economy<svg class="chev" viewBox="0 0 14 9"><polyline points="1,1 7,7 13,1" fill="none" stroke="#fff" stroke-width="1.6"/></svg></div>
  <div class="acc" style="left:169px;top:1569px;width:386px"><svg class="icon" viewBox="0 0 30 26"><path d="M3 18V10h24v8M3 14h24M5 18v4M25 18v4M7 10V6h16v4" fill="none" stroke="#fff" stroke-width="1.3"/></svg>High standard of living<svg class="chev" viewBox="0 0 14 9"><polyline points="1,1 7,7 13,1" fill="none" stroke="#fff" stroke-width="1.6"/></svg></div>
  <div class="acc" style="left:169px;top:1611px;width:386px;border:0"><svg class="icon" viewBox="0 0 30 26"><path d="M4 12a11 9 0 0 1 22 0z" fill="none" stroke="#fff" stroke-width="1.3"/><path d="M15 12v9a3 3 0 0 1-6 0" fill="none" stroke="#fff" stroke-width="1.3"/></svg>Exemplary pension system<svg class="chev" viewBox="0 0 14 9"><polyline points="1,1 7,7 13,1" fill="none" stroke="#fff" stroke-width="1.6"/></svg></div>
  <div class="illus" role="img" aria-label="Illustrated map of Switzerland with landmarks, mountains and lake, labelled federation, population and high living" style="left:614px;top:1169px;width:494px;height:366px;border-radius:40% 50% 45% 40%;background:radial-gradient(ellipse at 50% 55%,#ffffff,#e3edf5 55%,rgba(255,255,255,0) 72%)"></div>
</section>

<!-- IMMIGRATION -->
<section>
  <svg class="abs" style="left:120px;top:1815px" width="470" height="480" viewBox="0 0 470 480" role="img" aria-label="Three overlapping circles: EU/EFTA citizenship, immigrants from third country, overview of different work passes">
    <circle cx="340" cy="275" r="122" fill="none" stroke="var(--blue-pale)" stroke-width="5"/>
    <circle cx="340" cy="275" r="114" fill="var(--blue-ice)"/>
    <circle cx="137" cy="342" r="134" fill="none" stroke="var(--blue-pale)" stroke-width="6"/>
    <circle cx="137" cy="342" r="128" fill="#d2e2f0" opacity=".92"/>
    <circle cx="174" cy="137" r="134" fill="none" stroke="#2c5578" stroke-width="4" opacity=".5"/>
    <circle cx="174" cy="137" r="130" fill="var(--greenblue)" opacity=".9"/>
    <circle cx="208" cy="251" r="45" fill="#fff"/>
    <text x="174" y="150" text-anchor="middle" fill="#fff" font-family="Montserrat,sans-serif" font-weight="700" font-size="17">EU/EFTA</text>
    <text x="174" y="169" text-anchor="middle" fill="#fff" font-family="Montserrat,sans-serif" font-size="13">CITIZENSHIP</text>
    <text x="345" y="298" text-anchor="middle" fill="var(--navy)" font-family="Montserrat,sans-serif" font-weight="700" font-size="17">IMMIGRANTS</text>
    <text x="345" y="317" text-anchor="middle" fill="var(--navy)" font-family="Montserrat,sans-serif" font-size="14">FROM THIRD</text>
    <text x="345" y="335" text-anchor="middle" fill="var(--navy)" font-family="Montserrat,sans-serif" font-size="14">COUNTRY</text>
    <text x="137" y="373" text-anchor="middle" fill="var(--navy)" font-family="Montserrat,sans-serif" font-weight="700" font-size="17">OVERVIEW</text>
    <text x="137" y="392" text-anchor="middle" fill="var(--navy)" font-family="Montserrat,sans-serif" font-size="14">DIFFERENT WORK</text>
  </svg>
  <h2 class="abs" style="left:611px;top:1838px;font-size:34px;line-height:41px;font-weight:700">Immigrating to<br>Switzerland</h2>
  <p class="abs" style="left:611px;top:1928px;font-size:24px;font-weight:300">These options are available Switzerland</p>
  <p class="abs lead" style="left:611px;top:1976px;width:455px">Depending on which citizenship(s) an immigrant to Switzerland holds, immigration regulations differ. In this article we explain everything you need to know or consider about immigrating to Switzerland.</p>
  <div class="acc" style="left:617px;top:2068px;width:450px">Immigrants with EU/EFTA citizenship<svg class="chev" viewBox="0 0 14 9"><polyline points="1,1 7,7 13,1" fill="none" stroke="var(--greenblue)" stroke-width="1.6"/></svg></div>
  <div class="acc" style="left:617px;top:2117px;width:450px">Immigrants from a third country<svg class="chev" viewBox="0 0 14 9"><polyline points="1,1 7,7 13,1" fill="none" stroke="var(--greenblue)" stroke-width="1.6"/></svg></div>
  <div class="acc" style="left:617px;top:2166px;width:450px">Overview of the different work/establishment passes<svg class="chev" viewBox="0 0 14 9"><polyline points="1,1 7,7 13,1" fill="none" stroke="var(--greenblue)" stroke-width="1.6"/></svg></div>
</section>

<!-- LABOR LAW -->
<section>
  <div class="abs band-grey"></div>
  <h2 class="abs" style="left:161px;top:2430px;font-size:34px;font-weight:700">Labor Law in Switzerland</h2>
  <p class="abs" style="left:161px;top:2479px;font-size:26px;font-weight:300">An Overview</p>
  <p class="abs lead" style="left:163px;top:2530px;width:460px">Anyone who is gainfully employed in Switzerland is protected by Swiss labor law and is also subject to its rules. We explain everything you need to know about employment law in Switzerland and what rights and obligations you have as part of your employment.</p>
  <div class="acc" style="left:164px;top:2641px;width:445px">The employment contract<svg class="chev" viewBox="0 0 14 9"><polyline points="1,1 7,7 13,1" fill="none" stroke="var(--greenblue)" stroke-width="1.6"/></svg></div>
  <div class="acc" style="left:164px;top:2690px;width:445px">Probationary period<svg class="chev" viewBox="0 0 14 9"><polyline points="1,1 7,7 13,1" fill="none" stroke="var(--greenblue)" stroke-width="1.6"/></svg></div>
  <div class="acc" style="left:164px;top:2738px;width:445px">Termination of the employment relationship<svg class="chev" viewBox="0 0 14 9"><polyline points="1,1 7,7 13,1" fill="none" stroke="var(--greenblue)" stroke-width="1.6"/></svg></div>
  <div class="acc" style="left:164px;top:2787px;width:445px">When may the employer not terminate?<svg class="chev" viewBox="0 0 14 9"><polyline points="1,1 7,7 13,1" fill="none" stroke="var(--greenblue)" stroke-width="1.6"/></svg></div>
  <div class="illus" role="img" aria-label="Illustration of a hand holding a hammer in front of a blue map of Switzerland" style="left:650px;top:2420px;width:441px;height:390px;border-radius:45% 40% 50% 45%;background:linear-gradient(180deg,var(--greenblue),#2f6fa3 60%,#b8cde0)"></div>
</section>

<!-- DOUBLE TAXATION -->
<section>
  <div class="illus" role="img" aria-label="Illustration of tax documents surrounded by country flags and symbols" style="left:97px;top:3037px;width:471px;height:365px;border-radius:50%;background:radial-gradient(ellipse at 50% 55%,var(--blue-pale),var(--blue-ice) 55%,#fff 78%)"></div>
  <h2 class="abs" style="left:612px;top:3026px;font-size:28px;line-height:32px;font-weight:700;color:var(--greenblue)">Double taxation agreements<br>between Switzerland and<br>other countries</h2>
  <p class="abs lead" style="left:612px;top:3130px;width:465px">In order to avoid the income and assets of an individual living in Switzerland but having income or assets in another country, Switzerland has concluded double taxation agreements with many countries.</p>
  <div class="abs" style="left:614px;top:3229px;width:484px;font-size:13px;font-weight:700;color:var(--greenblue)">Taxation of income and assets<svg class="chev" viewBox="0 0 14 9" style="right:10px"><polyline points="1,8 7,2 13,8" fill="none" stroke="var(--navy-50)" stroke-width="1.6"/></svg></div>
  <p class="abs" style="left:614px;top:3252px;width:460px;font-size:11px;line-height:17.5px;color:var(--greenblue)">Double tax treaties are mostly aimed at taxing income. However, there are also treaties that take into account the assets as well. Double tax treaties are complex and are concluded individually between the two contracting states, so that usually no treaty is 100% similar to the other.</p>
  <p class="abs" style="left:614px;top:3335px;width:460px;font-size:11px;line-height:17.5px;color:var(--greenblue)">Therefore, it is always advisable to seek the advice of a tax expert when it comes to questions regarding the taxation of income and assets abroad.</p>
  <div class="abs" style="left:612px;top:3388px;width:486px;height:1px;background:var(--navy-25)"></div>
  <div class="abs" style="left:614px;top:3405px;width:484px;font-size:13px;line-height:17px;font-weight:700;color:var(--greenblue)">Countries with which Switzerland has a double<br>taxation agreement<svg class="chev" viewBox="0 0 14 9" style="right:10px;top:10px"><polyline points="1,1 7,7 13,1" fill="none" stroke="var(--navy-50)" stroke-width="1.6"/></svg></div>
</section>

<!-- INDIRECT TAXES -->
<section>
  <div class="abs band-dark2"></div>
  <h2 class="abs" style="left:154px;top:3645px;font-size:32px;font-weight:700;color:#fff">Indirect taxes in Switzerland</h2>
  <div class="abs" style="left:156px;top:3712px;width:440px;font-size:20px;font-weight:300;color:#fff">Value added tax<svg class="chev" viewBox="0 0 14 9" style="right:8px"><polyline points="1,8 7,2 13,8" fill="none" stroke="var(--navy-25)" stroke-width="1.6"/></svg></div>
  <p class="abs" style="left:157px;top:3747px;width:400px;font-size:11px;line-height:17.5px;color:#e1e8ee">As in many other countries, Switzerland also has a value added tax, which every consumer has to pay. Switzerland and Liechtenstein have a common VAT area, so that import/export or the procurement and provision of services in this community of states is treated as if it were a common country.</p>
  <a class="abs" style="left:157px;top:3845px;font-size:11px;color:#fff;text-decoration:underline">LEARN MORE</a>
  <div class="abs" style="left:154px;top:3885px;width:444px;height:1px;background:rgba(255,255,255,.35)"></div>
  <div class="abs" style="left:156px;top:3916px;width:440px;font-size:20px;font-weight:300;color:#fff">Indirect taxes incurred when moving<svg class="chev" viewBox="0 0 14 9" style="right:8px"><polyline points="1,1 7,7 13,1" fill="none" stroke="var(--navy-25)" stroke-width="1.6"/></svg></div>
  <div class="illus" role="img" aria-label="Outline map of Switzerland with the words indirect tax over a tax form, glasses, pencil, card and calculator" style="left:646px;top:3618px;width:434px;height:385px;border-radius:40%;background:radial-gradient(ellipse at 50% 60%,rgba(255,255,255,.55),rgba(181,191,200,.25) 45%,rgba(13,66,97,0) 72%)"></div>
</section>

</body>
</html>
```